Business card required for IT Consultancy Business - Bluefern Consulting.
Company provides the whole nine yards of services across IT Architecture, design and execution.
Basically we provide consulting services to help businesses make sure their technology is enabling their business strategy.
Design for front and back required.
We would like the front of the card to inlcude:
Name
Title
Mobile number
email address
www.BFQ.com.au
Company logos attached.
Thank you
Industry/Entity Type
Business
Contact Information for Business Card
Name
Title
Mobile number
email address
www.BFQ.com.au
Look and feel
Each slider illustrates characteristics of the customer's brand and the style your logo design should communicate.

```html
<!DOCTYPE html>
<html lang="en">
<head>
<meta charset="utf-8">
<title>Bluefern Consulting – Business Card</title>
<link href="https://fonts.googleapis.com/css2?family=Roboto:wght@300;400;500&display=swap" rel="stylesheet">
<style>
  :root {
    --backdrop: #4f93c6;
    --orange: #ec5a2c;
    --orange-light: #f0764a;
    --brand-blue: #2f78c0;
    --white: #ffffff;
    --paper: #f4f4f4;
    --ink-soft: rgba(255,255,255,0.9);
  }
  * { margin: 0; padding: 0; box-sizing: border-box; }
  html, body { width: 1200px; height: 1000px; overflow: hidden; }
  body {
    background: var(--backdrop);
    font-family: "Roboto", Arial, sans-serif;
    display: flex;
    align-items: center;
    justify-content: center;
    gap: 60px;
  }
  .card {
    width: 520px;
    height: 300px;
    border-radius: 4px;
    box-shadow: 0 14px 30px rgba(0,0,0,0.25);
    position: relative;
    overflow: hidden;
  }

  /* Front: contact side */
  .card-front {
    background: linear-gradient(135deg, var(--orange) 0%, var(--orange-light) 60%, var(--orange) 100%);
    color: var(--white);
    padding: 40px 44px;
  }
  .brand-lockup {
    display: flex;
    align-items: center;
    gap: 12px;
  }
  .brand-dot {
    width: 34px; height: 34px;
    border-radius: 50%;
    background: var(--white);
  }
  .brand-name {
    font-weight: 500;
    font-size: 26px;
    letter-spacing: 1px;
  }
  .card-front .brand-name { color: var(--white); }
  .identity {
    margin-top: 34px;
    padding-left: 16px;
    border-left: 1.5px solid var(--white);
  }
  .person-name {
    font-weight: 300;
    font-size: 20px;
    letter-spacing: 1.5px;
  }
  .person-title {
    font-weight: 500;
    font-size: 15px;
    color: var(--brand-blue);
    margin-top: 4px;
  }
  .contact-list {
    list-style: none;
    position: absolute;
    right: 44px;
    bottom: 40px;
  }
  .contact-list li {
    display: flex;
    align-items: center;
    gap: 10px;
    font-weight: 300;
    font-size: 15px;
    color: var(--ink-soft);
    margin-top: 8px;
  }
  .contact-icon { width: 14px; height: 14px; flex: none; }

  /* Back: brand side */
  .card-back {
    background: var(--paper);
    display: flex;
    align-items: center;
    justify-content: center;
  }
  .card-back .brand-dot { width: 46px; height: 46px; background: var(--orange); }
  .card-back .brand-name {
    color: var(--brand-blue);
    font-size: 38px;
  }
</style>
</head>
<body>

  <section class="card card-front" aria-label="Business card front">
    <div class="brand-lockup">
      <span class="brand-dot"></span>
      <span class="brand-name">Bluefern Consulting</span>
    </div>

    <div class="identity">
      <p class="person-name">MARLO VENN</p>
      <p class="person-title">CEO</p>
    </div>

    <ul class="contact-list">
      <li>
        <svg class="contact-icon" viewBox="0 0 14 14" aria-hidden="true">
          <rect x="3" y="0.5" width="8" height="13" rx="1.5" fill="none" stroke="#2f78c0" stroke-width="1.5"/>
          <circle cx="7" cy="11" r="0.9" fill="#2f78c0"/>
        </svg>
        041-2876-530
      </li>
      <li>
        <svg class="contact-icon" viewBox="0 0 14 14" aria-hidden="true">
          <rect x="0.5" y="2.5" width="13" height="9" fill="#2f78c0"/>
          <path d="M0.5 2.5 L7 8 L13.5 2.5" fill="none" stroke="#ffffff" stroke-width="1.2"/>
        </svg>
        hello@BFQ.com.au
      </li>
      <li>
        <svg class="contact-icon" viewBox="0 0 14 14" aria-hidden="true">
          <circle cx="7" cy="7" r="6.5" fill="#2f78c0"/>
          <path d="M0.5 7 H13.5 M7 0.5 C3.5 4 3.5 10 7 13.5 M7 0.5 C10.5 4 10.5 10 7 13.5" fill="none" stroke="#ffffff" stroke-width="0.9"/>
        </svg>
        www.BFQ.com.au
      </li>
    </ul>
  </section>

  <section class="card card-back" aria-label="Business card back">
    <div class="brand-lockup">
      <span class="brand-dot"></span>
      <span class="brand-name">Bluefern Consulting</span>
    </div>
  </section>

</body>
</html>
```